Start-Up Property Development Company Requires Word Press Website Design

A new property development company in Sydney requires a new website.
This version (Version 1) is very simple and will represent one, small aspect of what the company does, which is acquiring properties for redevelopment:

Needed:
- 1 page incorporating copy, logo and illustration.
- Email contact form.
- Contact information.

It will be expanded in the next few months to include another section for marketing homes for sale (Version 2). This section should sit on top of the Version 1 (in the top section of the same scrolling page).

So this initial design must be able to simply incorporate the expansion.

The site design needs to:
- Take up the entire width of the monitor.
- Not be too different from companies corporate look and feel.
- Be simple, functional and elegant.
- Have a long scroll (1 page) with navigation items at the top of the screen simply linking to the corresponding section lower in the page.

Reason: Not happy with the choice of designs. I'm wanting something clean and fresh and not too intensive with graphics.

```html
<!DOCTYPE html>
<html lang="en">
<head>
<meta charset="utf-8">
<title>Corwell Property</title>
<link href="https://fonts.googleapis.com/css2?family=Arimo:wght@400;700&family=Source+Sans+3:wght@400;600&display=swap" rel="stylesheet">
<style>
:root{
  --red:#c61f26;
  --red-soft:#f06a6e;
  --ink:#1f1f1f;
  --text:#4a4a4a;
  --line:#e3e3e3;
  --page:#ffffff;
  --footer:#231f20;
  --footer-text:#e6e6e6;
  --rss:#f0a91c;
  --fb:#3b5998;
  --tw:#3ba9e0;
}
*{box-sizing:border-box;margin:0;padding:0}
html,body{width:1200px;height:2590px;overflow:hidden;background:var(--page)}
body{position:relative;font-family:"Source Sans 3",sans-serif;color:var(--text)}
.abs{position:absolute}
.brand{font-family:"Arimo",sans-serif;font-weight:700;color:var(--ink);line-height:1;letter-spacing:1px}
.brand .l1{display:block;font-size:38px}
.brand .l2{display:block;font-size:24px;margin-top:4px;padding-left:30px}
.nav{top:42px;left:710px;display:flex;gap:44px;font-family:"Source Sans 3",sans-serif;font-size:14px;color:#333;text-transform:uppercase}
.nav a{color:inherit;text-decoration:none;position:relative}
.nav a.active{color:var(--red)}
.nav a.active::after{content:"";position:absolute;left:0;right:0;bottom:-12px;height:2px;background:var(--red)}
.nav a.active::before{content:"";position:absolute;left:50%;bottom:-17px;margin-left:-5px;border:5px solid transparent;border-top-color:var(--red)}
.social{top:35px;left:962px;display:flex;gap:10px}
.social span{width:36px;height:36px;display:block}
.social .rss{background:var(--rss)}.social .fb{background:var(--fb)}.social .tw{background:var(--tw)}
.hero{left:107px;top:121px;width:984px;height:480px;background:linear-gradient(180deg,#6f9ccc 0%,#b9d0e4 45%,#8fb2c8 62%,#5c6a72 100%)}
.hero h1{position:absolute;left:22px;top:84px;font-family:"Arimo",sans-serif;font-size:42px;font-weight:700;color:#fff;letter-spacing:1px}
.hero p{position:absolute;left:22px;top:141px;width:500px;font-size:16px;line-height:30px;color:#fff}
.dots{position:absolute;left:24px;top:416px;display:flex;gap:4px}
.dots i{width:11px;height:11px;border-radius:50%;background:#fff;display:block}
.dots i:first-child{background:var(--red)}
.heading{font-family:"Arimo",sans-serif;font-size:23px;font-weight:700;color:var(--ink);text-transform:uppercase}
.heading::after{content:"";display:block;width:76px;height:3px;background:var(--red);margin-top:17px}
.heading.light{color:#fff}.heading.light::after{background:#fff}
.body{font-size:14.5px;line-height:24px;color:var(--text)}
.btn{display:inline-block;width:130px;height:47px;line-height:47px;text-align:center;background:var(--red);color:#fff;font-size:16px;text-decoration:none}
.frame{width:473px;height:262px;border:1px solid var(--line);padding:17px 21px}
.frame .ph{width:100%;height:100%}
.ph-home{background:linear-gradient(180deg,#4b6fa8 0%,#a9b8cf 50%,#6a5a44 80%,#3b4a5a 100%)}
.ph-money{background:linear-gradient(135deg,#ffffff 20%,#c7d98a 45%,#6fae5a 60%,#f5f5f5 85%)}
.ph-room{background:linear-gradient(180deg,#d9d4cc 0%,#efece6 50%,#7a5a3e 100%)}
.ph-person{background:linear-gradient(180deg,#ffffff 0%,#ffffff 30%,#b98256 55%,#222 100%)}
.band{left:0;top:1632px;width:1200px;height:376px;background:var(--red)}
.field{position:absolute;background:#fff;font-size:13px;color:#8a8a8a;padding:0 13px;line-height:43px;height:43px;width:302px}
.field.msg{height:105px;line-height:1;padding-top:14px}
.submit{left:107px;top:1915px;width:145px;height:45px;line-height:45px;background:var(--red-soft);color:#fff;text-align:center;font-size:16px}
.footer{left:0;top:2400px;width:1200px;height:190px;background:var(--footer)}
.footer .info{position:absolute;left:107px;top:32px;color:var(--footer-text);font-size:14px;line-height:29px}
.footer .info h4{font-weight:400;font-size:16px;color:#fff;margin-bottom:2px}
.footer .brand{position:absolute;right:109px;top:34px;color:#e6e6e6;text-align:right}
.footer .copy{position:absolute;right:109px;top:122px;font-size:13px;color:var(--footer-text)}
</style>
</head>
<body>

<header>
  <div class="abs brand" style="left:107px;top:26px"><span class="l1">CORWELL</span><span class="l2">PROPERTY</span></div>
  <nav class="abs nav"><a class="active" href="#top">Home</a><a href="#contact">Contact Us</a></nav>
  <div class="abs social"><span class="rss" aria-label="Feed"></span><span class="fb" aria-label="Social page"></span><span class="tw" aria-label="Social feed"></span></div>
</header>

<section class="abs hero" role="img" aria-label="Modern white house with terrace pool overlooking the sea">
  <h1>CORWELL PROPERTY</h1>
  <p>Corwell Property is property development company located in Sydney. We are currently searching for properties to acquire and redevelop.</p>
  <div class="dots"><i></i><i></i><i></i><i></i></div>
</section>

<section class="abs" style="left:107px;top:649px;width:473px">
  <h2 class="heading">Distinctive Homes</h2>
  <div class="frame" style="margin-top:41px"><div class="ph ph-home" role="img" aria-label="Luxury home with palm trees and pool at dusk"></div></div>
  <p class="body" style="margin-top:30px">Lorem ipsum dolor sit amet, nec ludus minimum luptatum ad, choro erroribus interpretaris has et. Eam ad delenit forensibus, ut nec rebum eirmod iuvaret, vis in consetetur persequeris.</p>
  <a class="btn" style="margin-top:38px">More Info</a>
</section>

<section class="abs" style="left:618px;top:649px;width:473px">
  <h2 class="heading">Property Acquisition</h2>
  <div class="frame" style="margin-top:41px"><div class="ph ph-money" role="img" aria-label="House folded from banknotes under a magnifying glass"></div></div>
  <p class="body" style="margin-top:30px">Lorem ipsum dolor sit amet, nec ludus minimum luptatum ad, choro erroribus interpretaris has et. Eam ad delenit forensibus, ut nec rebum eirmod iuvaret, vis in consetetur persequeris.</p>
  <a class="btn" style="margin-top:38px">More Info</a>
</section>

<section class="abs" style="left:107px;top:1210px;width:984px">
  <h2 class="heading">Coming Soon</h2>
  <p class="body" style="margin-top:28px">Lorem ipsum dolor sit amet, nec ludus minimum luptatum ad, choro erroribus interpretaris has et. Eam ad delenit forensibus, ut nec rebum eirmod iuvaret, vis in consetetur persequeris. Lorem ipsum dolor sit amet, nec ludus minimum luptatum ad, choro erroribus interpretaris has et.</p>
</section>
<div class="abs ph-room" style="left:107px;top:1345px;width:300px;height:223px" role="img" aria-label="Bright living room interior with fireplace and staircase"></div>
<div class="abs" style="left:442px;top:1337px;width:640px">
  <p class="body">Ea propriae sapientem similique has, an mei velit feugait consulatu. Summo meliore voluptaria eu pro, an causae tincidunt repudiandae vis. Et detracto constituto theophrastus duo, te eam eripuit appetere periculis. Eu purto audiam vix.Vis nostrum reprehendunt te, perpetua.</p>
  <p class="body" style="margin-top:14px">Ea propriae sapientem similique has, an mei velit feugait consulatu. Summo meliore voluptaria eu pro, an causae tincidunt repudiandae vis. Et detracto constituto theophrastus duo, te eam eripuit appetere periculis. Eu purto audiam vix.Vis nostrum reprehendunt te.</p>
</div>
<a class="abs btn" style="left:442px;top:1523px">More Info</a>

<section class="abs band" id="contact">
  <h2 class="heading light" style="position:absolute;left:107px;top:45px">Quick Contact Form</h2>
  <p style="position:absolute;left:107px;top:110px;font-size:14px;color:#fff">Vis nostrum reprehendunt te, perpetua comprehensam vis no. Sed te purto dicat, ei qui rebum assum consetetur, senserit referrentur no sea.</p>
</section>
<div class="field" style="left:107px;top:1789px">Enter your first name</div>
<div class="field" style="left:428px;top:1789px">Enter your email</div>
<div class="field msg" style="left:748px;top:1789px">Message</div>
<div class="field" style="left:107px;top:1851px">Enter your last name</div>
<div class="field" style="left:428px;top:1851px">Enter your phone</div>
<div class="abs submit">Submit Now</div>

<section class="abs" style="left:107px;top:2063px;width:780px">
  <h2 class="heading">Shortly About Us</h2>
  <p class="body" style="margin-top:28px">No per zril prompta ullamcorper. Ex soluta blandit vis, mei vitae urbanitas an, ei altera apeirian insolens duo. His indoctum imperdiet ea, ius ad virtute posidonium. Sit in eligendi necessitatibus, eos an evertitur delicatissimi. Viderer postulant mea et. An agam ocurreret laboramus vis.</p>
  <p class="body" style="margin-top:10px">No per zril prompta ullamcorper. Ex soluta blandit vis, mei vitae urbanitas an, ei altera apeirian insolens duo. His indoctum imperdiet ea, ius ad virtute posidonium. Sit in eligendi necessitatibus, eos an evertitur delicatissimi.</p>
</section>
<div class="abs ph-person" style="left:905px;top:2080px;width:172px;height:180px" role="img" aria-label="Portrait of a smiling team member"></div>
<a class="abs btn" style="left:107px;top:2290px">More Info</a>

<footer class="abs footer">
  <div class="info">
    <h4>Contact Info</h4>
    Address : 412 Larchmont Lane<br>
    Brookfield, BF2 7QX<br>
    Telephone : +1 555 014 2287<br>
    E-mail : hello@corwellproperty.example
  </div>
  <div class="brand"><span class="l1">CORWELL</span><span class="l2">PROPERTY</span></div>
  <p class="copy">Copyright @ 2014 Corwell Property.All Rights Reserved.</p>
</footer>

</body>
</html>
```